Visitenkarten-Design für christliche Institution
Zielgruppe
Wir sind eine christliche Institution, die jungen Menschen im Alter von 17-30 Jahre helfen wollen, die Berufung in ihrem Leben zu finden.
Aufgabenstellung
Es sollte enhalten:
- Logo
- Adresse

```html
<!DOCTYPE html>
<html lang="de">
<head>
<meta charset="utf-8">
<title>Lebenswege – Visitenkarte</title>
<link href="https://fonts.googleapis.com/css2?family=Cinzel:wght@500;600&family=Montserrat:wght@400;500&display=swap" rel="stylesheet">
<style>
  :root {
    --stage: #e6e6e6;
    --paper: #f7f5f1;
    --gold-dark: #b8892a;
    --gold-mid: #d9b24c;
    --gold-light: #f3dc8e;
    --ink: #2b2b2b;
    --ink-soft: #555;
    --gold-gradient: linear-gradient(100deg, var(--gold-dark) 0%, var(--gold-light) 38%, var(--gold-mid) 62%, var(--gold-dark) 100%);
  }
  * { box-sizing: border-box; margin: 0; padding: 0; }
  html, body { width: 1200px; height: 900px; overflow: hidden; }
  body {
    background: radial-gradient(ellipse at 50% 40%, #f2f2f2 0%, var(--stage) 70%, #d6d6d6 100%);
    font-family: "Montserrat", sans-serif;
    color: var(--ink);
    position: relative;
  }
  .card {
    position: absolute;
    left: 290px;
    width: 620px;
    height: 360px;
    border-radius: 6px;
    overflow: hidden;
    box-shadow: 0 14px 34px rgba(0,0,0,.18);
  }

  /* back side */
  .card--back { top: 60px; background: var(--gold-gradient); }
  .card--back .brand {
    position: absolute; left: 0; right: 0; top: 150px;
    display: flex; align-items: center; justify-content: center; gap: 14px;
  }
  .card--back .brand-dot { width: 26px; height: 26px; border-radius: 50%; background: #fff; }
  .card--back .brand-name {
    font-family: "Cinzel", serif; font-weight: 600; font-size: 42px; color: #fff;
  }

  /* front side */
  .card--front { top: 480px; background: var(--paper); }
  .band-top {
    position: absolute; top: 0; left: 0; right: 0; height: 10px; background: var(--gold-gradient);
  }
  .band-top-step {
    position: absolute; top: 0; left: 0; width: 300px; height: 26px;
    background: var(--gold-gradient); border-bottom-right-radius: 18px;
  }
  .band-bottom {
    position: absolute; bottom: 22px; right: 0; width: 380px; height: 36px;
    background: var(--gold-gradient); border-radius: 18px 0 0 18px;
    display: flex; align-items: center; justify-content: center;
  }
  .email { font-size: 15px; letter-spacing: .3px; color: var(--ink); }
  .glow {
    position: absolute; border-radius: 50%;
    background: radial-gradient(circle, rgba(217,178,76,.22) 0%, rgba(217,178,76,.08) 55%, rgba(217,178,76,0) 72%);
  }
  .glow--top { width: 200px; height: 200px; top: 10px; right: -50px; }
  .glow--bottom { width: 170px; height: 170px; bottom: -60px; left: -40px; }

  .brand--front {
    position: absolute; left: 36px; top: 80px;
  }
  .brand--front .row { display: flex; align-items: center; gap: 10px; }
  .brand--front .brand-dot { width: 18px; height: 18px; border-radius: 50%; background: var(--gold-mid); }
  .brand--front .brand-name {
    font-family: "Cinzel", serif; font-weight: 600; font-size: 32px; color: var(--gold-dark);
  }
  .brand--front .tagline {
    margin: 4px 0 0 28px; font-size: 8px; letter-spacing: 2px; color: var(--ink-soft); text-transform: uppercase;
  }
  .person {
    position: absolute; left: 90px; top: 190px;
    font-family: "Cinzel", serif; font-weight: 500; font-size: 20px; letter-spacing: 1px; color: var(--ink);
  }
  .divider { position: absolute; left: 372px; top: 90px; width: 1px; height: 150px; background: #8a8a8a; }
  .contact { position: absolute; left: 392px; top: 88px; list-style: none; }
  .contact li { display: flex; align-items: center; gap: 10px; margin-bottom: 14px; }
  .contact .icon {
    width: 24px; height: 24px; border-radius: 50%; background: var(--ink);
    display: flex; align-items: center; justify-content: center; flex-shrink: 0;
  }
  .contact .lines { font-size: 12px; line-height: 1.45; color: var(--ink); }
</style>
</head>
<body>
  <section class="card card--back" aria-label="Rückseite">
    <div class="brand">
      <span class="brand-dot"></span>
      <span class="brand-name">Lebenswege</span>
    </div>
  </section>

  <section class="card card--front" aria-label="Vorderseite">
    <div class="band-top"></div>
    <div class="band-top-step"></div>
    <div class="glow glow--top" role="img" aria-label="dezente goldene Pinselkreis-Dekoration"></div>
    <div class="glow glow--bottom" role="img" aria-label="dezente goldene Pinselkreis-Dekoration"></div>

    <div class="brand brand--front">
      <div class="row">
        <span class="brand-dot"></span>
        <span class="brand-name">Lebenswege</span>
      </div>
      <p class="tagline">Jugendpastoral Halden</p>
    </div>

    <p class="person">JONAS BERGER</p>
    <div class="divider"></div>

    <ul class="contact">
      <li>
        <span class="icon">
          <svg width="12" height="14" viewBox="0 0 12 14"><path d="M6 0a5 5 0 0 0-5 5c0 3.6 5 9 5 9s5-5.4 5-9a5 5 0 0 0-5-5zm0 7a2 2 0 1 1 0-4 2 2 0 0 1 0 4z" fill="#fff"/></svg>
        </span>
        <span class="lines">Lindenweg 7<br>54321 Halden</span>
      </li>
      <li>
        <span class="icon">
          <svg width="12" height="12" viewBox="0 0 12 12"><path d="M2.4 0.6l1.8 0 1 2.8-1.3 1a6.5 6.5 0 0 0 3.7 3.7l1-1.3 2.8 1 0 1.8c0 .8-.7 1.4-1.5 1.3A10.5 10.5 0 0 1 1.1 2.1C1 1.3 1.6.6 2.4.6z" fill="#fff"/></svg>
        </span>
        <span class="lines">06123/456-789<br>0151 23456789</span>
      </li>
    </ul>

    <div class="band-bottom">
      <span class="email">jonas.berger@lebenswege-halden.de</span>
    </div>
  </section>
</body>
</html>
```